beauty salon

providing waxing services from a home base this must include which I will provide a price list and an address

Industry/Entity Type

Beauty Salon

Font styles to use
Script

Colors

Designer to choose colors to be used in the design.

```html
<!DOCTYPE html>
<html lang="en">
<head>
<meta charset="utf-8">
<title>Sienna's Haven Salon – Price List</title>
<link rel="stylesheet" href="https://fonts.googleapis.com/css2?family=Noto+Serif:wght@400;700&display=swap">
<style>
  :root {
    --bg-light: #eef3f5;
    --bg-mid: #cddde3;
    --bg-deep: #a9c3cc;
    --ink: #1c1c1c;
    --brand: #5a2fc2;
    --skin: #d9a88a;
    --skin-light: #ecd3c3;
    --eye-shadow: #8d6a9e;
    --towel: #eef0f0;
  }
  * { margin: 0; padding: 0; box-sizing: border-box; }
  html, body { width: 1200px; height: 900px; overflow: hidden; }
  body { font-family: "Noto Serif", Georgia, serif; color: var(--ink); }
  .canvas {
    position: relative; width: 1200px; height: 900px; overflow: hidden;
    background:
      radial-gradient(circle at 15% 20%, rgba(255,255,255,.85) 0, rgba(255,255,255,0) 28%),
      radial-gradient(circle at 80% 70%, rgba(255,255,255,.6) 0, rgba(255,255,255,0) 30%),
      radial-gradient(circle at 50% 55%, var(--bg-light) 0, var(--bg-mid) 60%, var(--bg-deep) 100%);
  }
  .brand-name {
    position: absolute; left: 0; width: 1260px; top: 108px; text-align: center;
    font-size: 28px; font-weight: 700; color: var(--brand);
  }
  .therapist {
    position: absolute; left: 330px; width: 600px; top: 158px; text-align: center;
    font-size: 21px; line-height: 29.5px; text-transform: uppercase;
  }
  .info { position: absolute; left: 38px; font-size: 18px; line-height: 26px; text-transform: uppercase; }
  .info .label { font-weight: 700; }
  .info .indent { display: block; }
  .address { top: 208px; }
  .address .indent { padding-left: 108px; }
  .hours { top: 316px; }
  .hours .indent { padding-left: 130px; }
  .section-title { position: absolute; font-size: 27px; font-weight: 400; text-transform: uppercase; white-space: nowrap; }
  .price-list { position: absolute; list-style: none; font-size: 18px; line-height: 25.3px; text-transform: uppercase; }
  .price-list li { display: flex; white-space: nowrap; }
  .price-list .service { flex: 0 0 auto; }
  .price-list .price { position: absolute; }
  .ladies-title { left: 38px; top: 424px; }
  .ladies-list { left: 38px; top: 477px; }
  .ladies-list .price { left: 188px; }
  .eye-title { left: 600px; top: 294px; }
  .eye-list { left: 600px; top: 342px; }
  .eye-list .price { left: 172px; }
  .mens-title { left: 605px; top: 608px; }
  .mens-list { left: 605px; top: 656px; }
  .mens-list .price { left: 205px; }
  .photo { position: absolute; }
  .photo-legs { left: 310px; top: 420px; width: 255px; height: 150px;
    background: linear-gradient(160deg, var(--towel) 0%, var(--skin-light) 55%, var(--skin) 100%); }
  .photo-underarm { left: 310px; top: 572px; width: 255px; height: 145px;
    background: linear-gradient(120deg, var(--skin) 0%, var(--skin-light) 55%, var(--towel) 100%); }
  .photo-face { left: 310px; top: 722px; width: 255px; height: 146px;
    background: linear-gradient(150deg, var(--skin-light) 0%, var(--skin) 60%, #c48f72 100%); }
  .photo-eyes { left: 860px; top: 336px; width: 312px; height: 176px;
    background: linear-gradient(180deg, var(--skin-light) 0%, var(--eye-shadow) 45%, var(--skin) 100%); }
  .photo-chest { left: 862px; top: 532px; width: 310px; height: 336px;
    background: linear-gradient(180deg, #f4f4f4 0%, var(--skin) 35%, #c08a6c 85%, #4d6a86 100%); }
</style>
</head>
<body>
<main class="canvas">
  <div class="brand-name">Sienna's Haven Salon</div>

  <p class="therapist">Beauty Therapist: Sienna<br>Diploma of Beauty Therapy<br>at Harlow Academy</p>

  <p class="info address"><span class="label">Address:</span> 12 Finch Lane
    <span class="indent">Riverbend</span>
    <span class="indent">Mobile: 0491 570 118</span></p>

  <p class="info hours"><span class="label">Now Open:</span>&nbsp; Wednesday 10am – 4pm
    <span class="indent">Fridays 10am-7pm</span>
    <span class="indent">Saturday 10am -4pm</span></p>

  <h2 class="section-title ladies-title">Lady's Waxing</h2>
  <ul class="price-list ladies-list">
    <li><span class="service">Eyebrow</span><span class="price">$8</span></li>
    <li><span class="service">Upper Lip</span><span class="price">$8</span></li>
    <li><span class="service">Chin</span><span class="price">$8</span></li>
    <li><span class="service">Face Wax</span><span class="price">$25</span></li>
    <li><span class="service">Bikini Line</span><span class="price">$15</span></li>
    <li><span class="service">G String</span><span class="price">$20</span></li>
    <li><span class="service">½ Brazilian</span><span class="price">$30</span></li>
    <li><span class="service">Full Brazilian</span><span class="price">$40</span></li>
    <li><span class="service">Half Arm</span><span class="price">$20</span></li>
    <li><span class="service">Upper Half Arm</span><span class="price">$20</span></li>
    <li><span class="service">Full Arm</span><span class="price">$25</span></li>
    <li><span class="service">Half Leg</span><span class="price">$15</span></li>
    <li><span class="service">Upper Leg</span><span class="price">$20</span></li>
    <li><span class="service">¾ Leg</span><span class="price">$25</span></li>
    <li><span class="service">Full Leg</span><span class="price">$35</span></li>
  </ul>

  <div class="photo photo-legs" role="img" aria-label="Photo of a leg being waxed with a strip"></div>
  <div class="photo photo-underarm" role="img" aria-label="Photo of an underarm wax treatment"></div>
  <div class="photo photo-face" role="img" aria-label="Photo of a facial wax being applied with a spatula"></div>

  <h2 class="section-title eye-title">Eye Enhancement</h2>
  <ul class="price-list eye-list">
    <li><span class="service">Eyebrow Tint</span><span class="price">$12</span></li>
    <li><span class="service">Eyelash Tint</span><span class="price">$15</span></li>
  </ul>
  <div class="photo photo-eyes" role="img" aria-label="Close-up photo of eyes with purple eye makeup and tinted lashes"></div>

  <h2 class="section-title mens-title">Men's Waxing</h2>
  <ul class="price-list mens-list">
    <li><span class="service">Eyebrow</span><span class="price">$10</span></li>
    <li><span class="service">Half Arm</span><span class="price">$20</span></li>
    <li><span class="service">Upper Half Arm</span><span class="price">$25</span></li>
    <li><span class="service">Full Arm</span><span class="price">$30</span></li>
    <li><span class="service">Half Leg</span><span class="price">$25</span></li>
    <li><span class="service">Full Leg</span><span class="price">$45</span></li>
    <li><span class="service">Chest Wax</span><span class="price">$40</span></li>
    <li><span class="service">Back Wax</span><span class="price">$35</span></li>
  </ul>
  <div class="photo photo-chest" role="img" aria-label="Photo of a man's torso with chest hair, showing chest waxing"></div>
</main>
</body>
</html>
```